Wordpress website design for Tavi Linkway-Africa

We need a website for a new consultancy and digital marketplace in Kenya called 'Tavi Linkway - Africa'. Please refer to the the attached document [Tavi Linkway Africa website brief] and contact me anytime.

Bests,
Philippa

Deadline extended to allow for additional revisions and refinements, ensuring that final designs align closely with project objectives and quality standards. This extra time will help incorporate valuable feedback and ensure the final output meets our high expectations.

```html
<!DOCTYPE html>
<html lang="en">
<head>
<meta charset="utf-8">
<title>Tavi Linkway Africa</title>
<link href="https://fonts.googleapis.com/css2?family=Montserrat:wght@400;500;600;700&display=swap" rel="stylesheet">
<style>
:root{
  --navy:#14146b;
  --green:#4a9a5c;
  --green-band:#458c57;
  --lavender:#ecebf6;
  --dark:#2e2e2e;
  --text:#222;
  --muted:#555;
  --white:#fff;
}
*{margin:0;padding:0;box-sizing:border-box}
html,body{width:1200px;height:3871px;overflow:hidden}
body{font-family:'Montserrat',sans-serif;color:var(--text);background:var(--white);position:relative}
.abs{position:absolute}
.center{left:0;width:1200px;text-align:center}
/* header */
.header{top:0;left:0;width:1200px;height:83px;background:var(--white);z-index:3}
.logo{left:110px;top:27px;font-size:28px;font-weight:700;letter-spacing:.5px;color:var(--navy)}
.logo span{color:var(--green)}
.nav{top:35px;left:468px;display:flex;gap:38px;font-size:14px;font-weight:500;color:#333}
.nav .active{text-decoration:underline;text-underline-offset:5px;color:var(--navy)}
.cart{left:1050px;top:30px}
.cart-badge{left:1071px;top:23px;width:15px;height:15px;border-radius:50%;background:var(--green);color:#fff;font-size:10px;text-align:center;line-height:15px}
/* hero */
.hero{top:83px;left:0;width:1200px;height:560px;background:linear-gradient(100deg,#8f8fcf 0%,#6d74a8 40%,#5e7d64 75%,#3f5e46 100%)}
.hero-title{top:228px;font-size:44px;line-height:56px;font-weight:600;color:#fff;letter-spacing:.5px}
.btn{display:block;text-align:center;font-weight:700;color:#fff;border-radius:8px 0 8px 0}
.btn-green{background:var(--green)}
.btn-navy{background:var(--navy)}
.hero-btn{left:512px;top:414px;width:169px;height:46px;line-height:46px;font-size:15px}
/* intro */
.intro{top:590px;left:0;width:1200px;height:600px;background:var(--lavender)}
.h2{font-size:38px;font-weight:500;letter-spacing:.5px;color:#111}
.bar{height:5px;width:97px;left:551px;border-radius:3px}
.bar-tri{background:linear-gradient(90deg,#111 0 35%,#c0262d 35% 55%,var(--green) 55%)}
.bar-ng{background:linear-gradient(90deg,var(--navy) 50%,var(--green) 50%)}
.intro-text{top:818px;left:230px;width:740px;text-align:center;font-size:14.5px;line-height:28.4px;color:#444}
.read-btn{left:514px;top:1013px;width:170px;height:47px;line-height:47px;font-size:15px}
/* services */
.sub-green{font-size:26px;font-weight:700;color:var(--green)}
.card{background:#fff;box-shadow:0 2px 10px rgba(0,0,0,.14)}
.svc{top:1435px;width:309px;height:165px;text-align:center}
.svc .ico{width:78px;height:78px;border-radius:50%;background:radial-gradient(circle,#2d3c8c 55%,#6aa86f 57%,#20306e 66%);margin:15px auto 0}
.svc p{font-size:23px;font-weight:600;margin-top:18px}
.arrow-l{left:34px;top:1489px}
.arrow-r{left:1111px;top:1489px}
/* marketplace */
.mk-sub{font-size:19px;font-weight:600}
.prod{top:1775px;width:309px;height:565px;text-align:center}
.prod .img{margin:6px 6px 0;height:254px}
.prod .brand{margin-top:30px;font-size:14px;font-weight:600;color:var(--green)}
.prod h3{margin-top:9px;font-size:21px;font-weight:600;line-height:33px;letter-spacing:.3px;white-space:nowrap}
.prod .desc{font-size:13px;line-height:30px;color:#555;white-space:nowrap;letter-spacing:-.2px}
.prod .desc b{color:var(--navy);font-weight:700}
.prod .rate{margin-top:8px;font-size:14px;font-weight:600}
.prod .rate span{color:#f0b400;letter-spacing:-1px}
.prod .price{margin-top:6px;font-size:22px}
.prod .price s{font-size:14px;color:#555;margin-right:6px}
.prod .btn{position:absolute;left:68px;bottom:26px;width:169px;height:46px;line-height:46px;font-size:15px}
.dots{top:2394px;left:550px;display:flex;gap:7px}
.dots i{display:block;width:15px;height:15px;border:2px solid var(--navy);border-radius:50%}
.dots i.on{background:var(--navy)}
/* featured */
.featured{top:2450px;left:0;width:1200px;height:790px;background:var(--green-band)}
.feat-title{left:112px;top:2588px;font-size:38px;font-weight:600;color:#fff}
.feat-bar{left:112px;top:2663px;width:97px;height:5px;background:#fff;border-radius:3px}
.feat{top:2712px;width:370px;height:353px;background:#fff;border-radius:0 0 4px 4px;overflow:hidden}
.feat .img{height:252px}
.feat h4{margin:26px 0 0 21px;font-size:20px;font-weight:600}
.feat a{display:block;margin:10px 0 0 27px;font-size:13px;font-weight:700;color:var(--green);text-decoration:underline;text-underline-offset:3px}
/* newsletter + footer */
.footer{top:3200px;left:0;width:1200px;height:671px;background:var(--dark)}
.sub-title{top:3290px;font-size:38px;font-weight:600;color:#fff}
.field{top:3372px;height:52px;background:#fff;border-radius:26px;padding-left:20px;font-size:16px;line-height:52px;color:#222}
.sub-btn{left:909px;top:3377px;width:170px;height:46px;line-height:46px;font-size:15px}
.rule{left:108px;width:977px;height:1px;background:#5a5a5a}
.f-logo{left:120px;top:3553px;width:240px;text-align:center;font-size:34px;font-weight:700;line-height:39px;color:#fff}
.social{top:3670px;left:120px;display:flex;gap:22px}
.social i{display:block;width:26px;height:26px;border-radius:50%;background:#fff}
.col h5{font-size:18px;font-weight:600;color:#fff;margin-bottom:14px}
.col li{list-style:none;font-size:14px;color:#fff;height:34px;display:flex;align-items:center;gap:10px}
.col li svg{flex:none}
.contact li{height:auto;margin-bottom:20px;align-items:flex-start;line-height:24px}
.contact .ci{width:32px;height:32px;border-radius:50%;background:#fff;flex:none;display:flex;align-items:center;justify-content:center;margin-top:2px}
.copy{left:108px;top:3820px;font-size:14px;color:#fff}
.pay{left:660px;top:3822px;display:flex;gap:6px}
.pay i{display:block;width:33px;height:21px;background:#fff;border-radius:3px}
</style>
</head>
<body>

<header class="abs header">
  <div class="abs logo">TAVI <span>LINKWAY</span></div>
  <nav class="abs nav">
    <span class="active">HOME</span><span>SERVICES</span><span>MARKETPLACE</span><span>ABOUT US</span><span>CONTACT</span>
  </nav>
  <svg class="abs cart" width="28" height="26" viewBox="0 0 28 26" fill="none" stroke="#222" stroke-width="2"><path d="M1 2h4l4 15h14l3-10H7"/><circle cx="11" cy="22" r="2"/><circle cx="21" cy="22" r="2"/></svg>
  <div class="abs cart-badge">0</div>
</header>

<section class="abs hero" role="img" aria-label="Photo of business people shaking hands in a meeting, tinted purple and green"></section>
<h1 class="abs center hero-title">EMPOWERING INNOVATIONS &amp;<br>DIGITAL TRANSFORMATION<br>ACROSS AFRICA.</h1>
<a class="abs btn btn-green hero-btn">GET STARTED</a>

<section class="abs intro"></section>
<svg class="abs" style="top:580px;left:0" width="1200" height="70"><path d="M0 10 Q600 95 1200 5 V70 H0Z" fill="#ecebf6"/></svg>
<h2 class="abs center h2" style="top:708px">INTRODUCTION ABOUT TAVI LINKWAY</h2>
<div class="abs bar bar-tri" style="top:783px"></div>
<p class="abs intro-text">Tavi Linkway Africa is a consultancy firm and digital marketplace dedicated to supporting Africa's digital transformation. We provide data-driven insights, strategic guidance, customised solutions to empower public and private sectors.<br>We aim to tackle complex challenges, optimize operations, and unlock growth through innovative technology.<br>Our marketplace offers a curated selection of digital products and tools designed to support strategic</p>
<a class="abs btn btn-green read-btn">READ MORE</a>
<svg class="abs" style="top:1160px;left:0" width="1200" height="40"><path d="M0 30 Q600 -10 1200 30 V40 H0Z" fill="#fff"/></svg>

<h2 class="abs center h2" style="top:1250px">QUICK LINKS</h2>
<div class="abs bar bar-ng" style="top:1326px"></div>
<div class="abs center sub-green" style="top:1372px">OUR SERVICES</div>

<svg class="abs arrow-l" width="56" height="56"><circle cx="28" cy="28" r="26" fill="#fff" stroke="#222" stroke-width="2"/><path d="M32 17 L21 28 L32 39" stroke="#222" stroke-width="4" fill="none"/></svg>
<div class="abs card svc" style="left:110px"><div class="ico" role="img" aria-label="Digital strategy icon"></div><p>Digital Strategy</p></div>
<div class="abs card svc" style="left:444px"><div class="ico" role="img" aria-label="Technical expertise icon"></div><p>Technical Expertise</p></div>
<div class="abs card svc" style="left:777px"><div class="ico" role="img" aria-label="Data analytics icon"></div><p>Data Analytics</p></div>
<svg class="abs arrow-r" width="56" height="56"><circle cx="28" cy="28" r="26" fill="#14146b"/><path d="M24 17 L35 28 L24 39" stroke="#fff" stroke-width="4" fill="none"/></svg>

<div class="abs center sub-green" style="top:1668px">MARKETPLACE</div>
<div class="abs center mk-sub" style="top:1726px">e-Commerce for digital products</div>

<div class="abs card prod" style="left:110px">
  <div class="img" role="img" aria-label="Laptop with business charts and dashboards" style="background:linear-gradient(135deg,#dfe6f2,#6a8fc4 60%,#3e5c9a)"></div>
  <div class="brand">TAVI LINKWAY</div>
  <h3>DIGITAL STRATEGY</h3>
  <p class="desc">Lorem Ipsum is simply dummy text of<br>the printing and <b>READ MORE</b></p>
  <div class="rate"><span>★★★★★</span> (500)</div>
  <div class="price"><s>$93.88</s>$54.49</div>
  <a class="btn btn-navy">ADD TO CART</a>
</div>
<div class="abs card prod" style="left:444px">
  <div class="img" role="img" aria-label="Hands holding a glowing AI interface" style="background:linear-gradient(135deg,#0d2a33,#1f5a66 55%,#0b1d24)"></div>
  <div class="brand">TAVI LINKWAY</div>
  <h3>ARTIFICIAL<br>INTELLIGENCE (AI)</h3>
  <p class="desc">Lorem Ipsum is <b>READMORE</b></p>
  <div class="rate"><span>★★★★★</span> (500)</div>
  <div class="price"><s>$93.88</s>$54.49</div>
  <a class="btn btn-navy">ADD TO CART</a>
</div>
<div class="abs card prod" style="left:777px">
  <div class="img" role="img" aria-label="Hand touching an expert advice digital screen" style="background:linear-gradient(135deg,#1b2e4a,#3d6a96 55%,#142238)"></div>
  <div class="brand">TAVI LINKWAY</div>
  <h3>TECHNICAL EXPERTISE</h3>
  <p class="desc">Lorem Ipsum is simply dummy text of<br>the printing and typesetting industry.</p>
  <div class="rate"><span>★★★★★</span> (500)</div>
  <div class="price"><s>$93.88</s>$54.49</div>
  <a class="btn btn-navy">ADD TO CART</a>
</div>
<div class="abs dots"><i class="on"></i><i></i><i></i><i></i><i></i></div>

<section class="abs featured"></section>
<svg class="abs" style="top:2440px;left:0" width="1200" height="80"><path d="M0 0 H1200 V18 Q600 120 0 14Z" fill="#fff"/></svg>
<div class="abs feat-title">FEATURED PRODUCTS</div>
<div class="abs feat-bar"></div>
<svg class="abs" style="left:978px;top:2596px" width="30" height="24"><path d="M28 12H4M13 3L4 12l9 9" stroke="#8aa896" stroke-width="3" fill="none"/></svg>
<svg class="abs" style="left:1024px;top:2584px" width="64" height="50"><rect x="1.5" y="1.5" width="61" height="47" rx="6" fill="none" stroke="#fff" stroke-width="2"/><path d="M19 25h25M35 15l10 10-10 10" stroke="#fff" stroke-width="3.5" fill="none"/></svg>

<div class="abs feat" style="left:110px">
  <div class="img" role="img" aria-label="Report template covers with landscape photos" style="background:linear-gradient(90deg,#e8eef0,#a9c0c6 45%,#c99a55 70%,#2a3a45)"></div>
  <h4>Templates</h4><a>LEARN MORE</a>
</div>
<div class="abs feat" style="left:497px">
  <div class="img" role="img" aria-label="E-book cover and printed pages" style="background:linear-gradient(135deg,#f0f2f5,#2f7fc4 50%,#e6e9ee)"></div>
  <h4>E-Books</h4><a>LEARN MORE</a>
</div>
<div class="abs feat" style="left:884px;width:316px;border-radius:0">
  <div class="img" role="img" aria-label="Developer typing code on a laptop" style="background:linear-gradient(135deg,#d9dde3,#56606d 55%,#2c323a)"></div>
  <h4>Software</h4><a>LEARN MORE</a>
</div>

<section class="abs footer"></section>
<svg class="abs" style="top:3165px;left:0" width="1200" height="60"><path d="M0 50 Q600 5 1200 50 V60 H0Z" fill="#2e2e2e"/></svg>
<h2 class="abs center sub-title">SUBSCRIBE TO OUR NEWSLETTER</h2>
<div class="abs field" style="left:108px;width:280px">Name</div>
<div class="abs field" style="left:408px;width:479px">Enter Your Email</div>
<a class="abs btn btn-green sub-btn">SUBSCRIBE</a>
<div class="abs rule" style="top:3480px"></div>

<div class="abs f-logo">TAVI<br>LINKWAY</div>
<div class="abs social"><i></i><i></i><i></i><i></i><i></i></div>

<div class="abs col" style="left:428px;top:3540px">
  <h5>QUICK LINKS</h5>
  <ul>
    <li><svg width="12" height="12"><path d="M1 6h9M6 2l4 4-4 4" stroke="#fff" stroke-width="2" fill="none"/></svg>Home</li>
    <li><svg width="12" height="12"><path d="M1 6h9M6 2l4 4-4 4" stroke="#fff" stroke-width="2" fill="none"/></svg>Services</li>
    <li><svg width="12" height="12"><path d="M1 6h9M6 2l4 4-4 4" stroke="#fff" stroke-width="2" fill="none"/></svg>Marketplace</li>
    <li><svg width="12" height="12"><path d="M1 6h9M6 2l4 4-4 4" stroke="#fff" stroke-width="2" fill="none"/></svg>About Us</li>
    <li><svg width="12" height="12"><path d="M1 6h9M6 2l4 4-4 4" stroke="#fff" stroke-width="2" fill="none"/></svg>Contact</li>
  </ul>
</div>
<div class="abs col" style="left:660px;top:3540px">
  <h5>HELP LINKS</h5>
  <ul>
    <li><svg width="12" height="12"><path d="M1 6h9M6 2l4 4-4 4" stroke="#fff" stroke-width="2" fill="none"/></svg>Our Blog</li>
    <li><svg width="12" height="12"><path d="M1 6h9M6 2l4 4-4 4" stroke="#fff" stroke-width="2" fill="none"/></svg>FAQ</li>
    <li><svg width="12" height="12"><path d="M1 6h9M6 2l4 4-4 4" stroke="#fff" stroke-width="2" fill="none"/></svg>Terms of use</li>
    <li><svg width="12" height="12"><path d="M1 6h9M6 2l4 4-4 4" stroke="#fff" stroke-width="2" fill="none"/></svg>Privacy Policy</li>
    <li><svg width="12" height="12"><path d="M1 6h9M6 2l4 4-4 4" stroke="#fff" stroke-width="2" fill="none"/></svg>Support Links</li>
  </ul>
</div>
<div class="abs col contact" style="left:873px;top:3540px">
  <h5>CONTACT US</h5>
  <ul>
    <li><span class="ci"><svg width="14" height="18"><path d="M7 17C2 10 1 8 1 6a6 6 0 0112 0c0 2-1 4-6 11z" fill="#2e2e2e"/><circle cx="7" cy="6" r="2" fill="#fff"/></svg></span>Mbaraki Rd, Kilimani,<br>Nairobi Kenya</li>
    <li><span class="ci"><svg width="16" height="16"><path d="M3 1l3 3-2 2c1 2 3 4 5 5l2-2 3 3-2 3C6 14 2 10 1 3z" fill="#2e2e2e"/></svg></span>+254 700 000 000</li>
    <li><span class="ci"><svg width="16" height="12"><rect x="0" y="0" width="16" height="12" rx="2" fill="#2e2e2e"/><path d="M1 1l7 6 7-6" stroke="#fff" fill="none"/></svg></span>info@tavilinkway.com</li>
  </ul>
</div>

<div class="abs rule" style="top:3785px"></div>
<div class="abs copy">Copyrights@2024. TAVI LINKWAY. All Rights Reserved</div>
<div class="abs pay"><i></i><i></i><i></i><i></i><i></i><i></i><i></i><i></i><i></i><i></i><i></i></div>

</body>
</html>
```